We sell companies excess stock for them

We need a business card for a company based in New Zealand called 'StockHarbor'.

Check out our website to get an idea www.stockharbor.example

We help other businesses to;
- Sell Excess Stock
- Manage Product Returns
- Sell Company Assets

Our logo is attached for your reference
The font used is 'RifficFree-Bold'

Target Market(s)

Businesses

Industry/Entity Type

Business

Contact Information for Business Card

Name: Mark Pellow
Phone: 027 846 2093
email: markpellow@stockharbor.example
website: www.stockharbor.example

Font styles to use
Other font styles liked:
• Unsure

Colors
9bcb3b

Requirements
Must have
• coming soon
Nice to have
• coming soon
Should not have
• coming soon

```html
<!DOCTYPE html>
<html lang="en">
<head>
<meta charset="utf-8">
<title>StockHarbor — Business Card</title>
<link href="https://fonts.googleapis.com/css2?family=Fredoka:wght@700&family=Lato:wght@400&display=swap" rel="stylesheet">
<style>
  :root {
    --green: #8dc63f;
    --ink: #2f2a28;
    --paper: #ffffff;
    --card-dark: #1f1f1f;
    --card-dark-light: #333333;
    --backdrop: #161616;
    --muted: #3a3a3a;
  }
  * { margin: 0; padding: 0; box-sizing: border-box; }
  html, body {
    width: 1200px; height: 897px; overflow: hidden;
    background: var(--backdrop);
  }
  .canvas { position: relative; width: 1200px; height: 897px; }

  .card {
    position: absolute; left: 303px; width: 595px; height: 338px;
    border-radius: 18px; overflow: hidden;
  }
  .card--front { top: 92px; background: var(--paper); }
  .card--back {
    top: 469px;
    background: radial-gradient(circle at 88% 78%, var(--card-dark-light) 0%, var(--card-dark) 55%);
  }

  .mascot {
    position: absolute; left: 74px; top: 80px; width: 168px; height: 180px;
    border-radius: 50%;
    background: radial-gradient(circle at 50% 45%, #f0a93a 0%, #8dc63f 55%, #ffffff 72%);
  }
  .divider {
    position: absolute; left: 274px; top: 82px; width: 2px; height: 176px;
    background: var(--green);
  }

  .details { position: absolute; left: 306px; top: 0; right: 0; }
  .wordmark {
    font-family: "Fredoka", sans-serif; font-weight: 700; color: var(--ink);
    line-height: 1; letter-spacing: -0.5px;
  }
  .details .wordmark { position: absolute; top: 79px; font-size: 38px; }

  .person-name {
    position: absolute; top: 138px;
    font-family: "Fredoka", sans-serif; font-weight: 700; font-size: 25px;
    color: var(--ink); text-transform: uppercase; line-height: 1;
  }
  .person-name .surname { color: var(--green); }
  .person-role {
    position: absolute; top: 166px;
    font-family: "Lato", sans-serif; font-size: 16px; color: var(--muted);
  }

  .contact-list { position: absolute; top: 203px; list-style: none; }
  .contact-list li {
    display: flex; align-items: center; height: 19.5px;
    font-family: "Lato", sans-serif; font-size: 15px; color: var(--ink);
  }
  .contact-list svg { width: 12px; height: 12px; margin-right: 12px; fill: var(--green); }
  .accent { color: var(--green); }

  .card--back .wordmark {
    position: absolute; left: 0; right: 0; top: 135px;
    text-align: center; font-size: 68px; color: #ffffff;
  }
  .back-url {
    position: absolute; left: 0; right: 0; top: 297px; text-align: center;
    font-family: "Lato", sans-serif; font-size: 16px; letter-spacing: 2px; color: #ffffff;
  }
</style>
</head>
<body>
<main class="canvas">
  <section class="card card--front">
    <div class="mascot" role="img" aria-label="Cartoon courier mascot in a green cap carrying an orange parcel"></div>
    <div class="divider"></div>
    <div class="details">
      <div class="wordmark">StockHarbor</div>
      <div class="person-name">Mark <span class="surname">Pellow</span></div>
      <div class="person-role">Director</div>
      <ul class="contact-list">
        <li>
          <svg viewBox="0 0 24 24" aria-hidden="true"><path d="M6.6 10.8a15.1 15.1 0 0 0 6.6 6.6l2.2-2.2c.3-.3.7-.4 1-.2 1.1.4 2.3.6 3.6.6.6 0 1 .4 1 1V20c0 .6-.4 1-1 1A17 17 0 0 1 3 4c0-.6.4-1 1-1h3.5c.6 0 1 .4 1 1 0 1.3.2 2.5.6 3.6.1.3 0 .7-.2 1z"/></svg>
          027 846 2093
        </li>
        <li>
          <svg viewBox="0 0 24 24" aria-hidden="true"><path d="M2 5h20v14H2z M2 5l10 8 10-8" /></svg>
          markpellow@stockharbor.example
        </li>
        <li>
          <svg viewBox="0 0 24 24" aria-hidden="true"><path d="M12 2a10 10 0 1 0 0 20 10 10 0 0 0 0-20zm6.9 6h-2.9a15 15 0 0 0-1.4-3.6A8 8 0 0 1 18.9 8zM12 4c.8 1.2 1.5 2.5 1.9 4h-3.8c.4-1.5 1.1-2.8 1.9-4zM4.3 14a8 8 0 0 1 0-4h3.4a16 16 0 0 0 0 4zm.8 2h2.9c.3 1.3.8 2.5 1.4 3.6A8 8 0 0 1 5.1 16zM8 8H5.1a8 8 0 0 1 4.3-3.6C8.8 5.5 8.3 6.7 8 8zm4 12c-.8-1.2-1.5-2.5-1.9-4h3.8c-.4 1.5-1.1 2.8-1.9 4zm2.3-6H9.7a14 14 0 0 1 0-4h4.6a14 14 0 0 1 0 4zm.3 5.6c.6-1.1 1.1-2.3 1.4-3.6h2.9a8 8 0 0 1-4.3 3.6zm1.7-5.6a16 16 0 0 0 0-4h3.4a8 8 0 0 1 0 4z"/></svg>
          www.<span class="accent">stockharbor</span>.example
        </li>
      </ul>
    </div>
  </section>

  <section class="card card--back">
    <div class="wordmark">StockHarbor</div>
    <div class="back-url">www.<span class="accent">stockharbor</span>.example</div>
  </section>
</main>
</body>
</html>
```